VOLT - Monitoring Natural Hazards from Space Web Application

KORMEL Sarl is a Luxembourg based Space-Startup that works in the field of Earth Observation. KORMEL is a platform able to extract value-added information from satellite data and is specialized in mapping Natural Disaster (floods, fires etc).

We are now developing a new vertical tool, called VOLT, dedicated to the monitoring of natural hazards in Humanitarian Camps around the world.

The goal of VOLT is to hide to the users' all the complexity of the Satellite Image processing and just provide them the results.

This project require to Design 4 pages of VOLT:
• Public Home Page (Code - V01)
• Dashboard (private Home Page) (Code - V03)
• Monitor (web GIS) (Code - V14)
• Registration Page (Code - V04)

We would like to provide the required time to make a good job.

Target Market(s)

Humanitarian Agencies, Goverments

Coding

Coded - Design and coding required

Number of Pages Required

4 page

Font styles to use
Other font styles liked:
• see the manual attached

Requirements
Must have
• 4 pages. One Home, one form, one dashboard and one web map.
Nice to have
• Please read the attachment with all the detailed instructions

```html
<!DOCTYPE html>
<html lang="en">
<head>
<meta charset="UTF-8">
<title>VOLT Dashboard</title>
<link href="https://fonts.googleapis.com/css2?family=Lexend:wght@400;500;600;700&family=Space+Mono&display=swap" rel="stylesheet">
<style>
:root{
  --teal:#2a4a58;
  --bg:#ebf3fd;
  --white:#ffffff;
  --amber:#f1b83f;
  --alert:#f26b3a;
  --ink:#111;
  --map:#7ccbea;
  --muted:#b8b8b8;
}
*{margin:0;padding:0;box-sizing:border-box}
html,body{width:1200px;height:853px;overflow:hidden}
body{font-family:"Lexend",sans-serif;background:var(--bg);position:relative;color:var(--ink)}
.sidebar{position:absolute;left:0;top:0;width:233px;height:853px;background:var(--white)}
.brand{position:absolute;left:17px;top:26px;display:flex;align-items:center;gap:8px}
.brand-dot{width:28px;height:28px;border-radius:50%;border:2px solid var(--amber)}
.brand-name{font-size:22px;font-weight:400;color:var(--teal);letter-spacing:3px}
.collapse{position:absolute;left:212px;top:34px}
.menu-label{position:absolute;left:10px;font-size:10px;color:var(--teal);font-weight:500}
.nav-item{position:absolute;left:0;width:233px;height:33px;display:flex;align-items:center;gap:12px;padding-left:10px;font-size:15px;font-weight:500;color:var(--teal)}
.nav-item svg{width:19px;height:19px;flex:none}
.nav-item.active{background:var(--teal);color:var(--white);border-left:4px solid var(--amber);padding-left:10px}
.upgrade{position:absolute;left:52px;top:712px;width:127px;height:73px;background:var(--white);border-radius:6px;box-shadow:0 6px 14px rgba(0,0,0,.12);text-align:center}
.upgrade-title{margin-top:13px;font-size:10px;font-weight:500;color:var(--teal)}
.upgrade-star{color:var(--amber);margin-left:8px}
.upgrade-text{font-family:"Space Mono",monospace;font-size:6px;line-height:7px;color:#555;margin-top:6px}
.upgrade-btn{position:absolute;left:34px;top:63px;width:59px;height:20px;border-radius:10px;background:var(--teal);color:var(--white);font-size:6px;line-height:20px}
.copyright{position:absolute;left:75px;top:829px;font-size:10px;color:var(--muted)}
.page-title{position:absolute;left:285px;top:23px;font-size:34px;font-weight:600;color:var(--teal)}
.search{position:absolute;left:593px;top:32px;width:300px;height:26px;background:var(--white);border-radius:13px;font-size:10px;padding-left:10px;line-height:26px;color:#222}
.search svg{position:absolute;right:10px;top:6px}
.round-btn{position:absolute;top:28px;width:32px;height:32px;border-radius:50%;background:var(--white);display:flex;align-items:center;justify-content:center;font-size:10px;font-weight:600}
.map{position:absolute;left:283px;top:106px;width:867px;height:462px;border-radius:6px;background:linear-gradient(90deg,var(--map) 0%,#a9d6b8 25%,var(--map) 45%,#e6e2cc 70%,#d8e2b8 100%)}
.map-tool{position:absolute;left:297px;width:32px;height:32px;border-radius:50%;background:var(--white);display:flex;align-items:center;justify-content:center}
.card{position:absolute;left:283px;width:300px;height:120px;background:var(--white);border-radius:6px}
.card-label{position:absolute;font-size:13px}
.stat{position:absolute;left:86px;top:50px;font-size:40px;font-weight:600;color:var(--amber)}
.alert-text{position:absolute;left:106px;top:45px;font-size:19px;font-weight:500;color:var(--alert);line-height:23px}
.events-label{position:absolute;left:608px;top:585px;font-size:13px}
.event{position:absolute;left:608px;width:512px;height:64px;background:var(--white);border-radius:5px;padding:10px 0 0 10px}
.event-type{font-size:19px;font-weight:500;color:var(--amber);line-height:24px}
.event-meta{font-size:15px;line-height:22px}
.scroll-track{position:absolute;left:1145px;top:610px;width:2px;height:243px;background:#dfe6ee}
.scroll-thumb{position:absolute;left:1143px;top:620px;width:6px;height:68px;background:var(--amber);border-radius:2px}
</style>
</head>
<body>
<aside class="sidebar">
  <div class="brand"><span class="brand-dot"></span><span class="brand-name">VOLT</span></div>
  <svg class="collapse" width="11" height="13" viewBox="0 0 11 13"><path d="M11 0V13L0 6.5Z" fill="#2a4a58"/></svg>
  <div class="menu-label" style="top:119px">Main Menu</div>
  <div class="nav-item active" style="top:147px"><svg viewBox="0 0 24 24" fill="none" stroke="currentColor" stroke-width="2"><path d="M3 11L12 3l9 8v10H3z"/></svg>Dashboard</div>
  <div class="nav-item" style="top:192px"><svg viewBox="0 0 24 24" fill="#2a4a58"><circle cx="12" cy="6" r="4"/><circle cx="6" cy="18" r="4"/><circle cx="18" cy="18" r="4"/></svg>My Organization</div>
  <div class="nav-item" style="top:228px"><svg viewBox="0 0 24 24" fill="none" stroke="currentColor" stroke-width="2"><circle cx="9" cy="8" r="4"/><path d="M2 21c0-4 3-7 7-7s7 3 7 7M16 4a4 4 0 010 8M18 14c2 1 4 3 4 7"/></svg>My Users</div>
  <div class="nav-item" style="top:267px"><svg viewBox="0 0 24 24" fill="none" stroke="currentColor" stroke-width="2"><rect x="2" y="4" width="20" height="13"/><path d="M8 21h8M12 17v4"/></svg>Monitor</div>
  <div class="nav-item" style="top:305px"><svg viewBox="0 0 24 24" fill="none" stroke="currentColor" stroke-width="2"><path d="M2 5l6-2 8 3 6-2v15l-6 2-8-3-6 2zM8 3v16M16 6v16"/></svg>Area of Operations</div>
  <div class="nav-item" style="top:342px"><svg viewBox="0 0 24 24" fill="none" stroke="currentColor" stroke-width="2"><circle cx="12" cy="12" r="3"/><circle cx="12" cy="12" r="9" stroke-dasharray="4 2"/></svg>Settings</div>
  <div class="menu-label" style="top:416px">Account</div>
  <div class="nav-item" style="top:436px"><svg viewBox="0 0 24 24" fill="none" stroke="currentColor" stroke-width="2"><circle cx="12" cy="7" r="4"/><path d="M4 22c0-5 4-8 8-8s8 3 8 8"/></svg>Profile</div>
  <div class="nav-item" style="top:473px"><svg viewBox="0 0 24 24"><rect x="2" y="2" width="20" height="20" rx="2" fill="#2a4a58"/><text x="12" y="18" font-size="15" text-anchor="middle" fill="#fff" font-family="sans-serif">?</text></svg>Help &amp; Information</div>
  <div class="upgrade">
    <div class="upgrade-title">Upgrade to PRO<span class="upgrade-star">★</span></div>
    <div class="upgrade-text">Get 1 Month free and<br>Unlock All Pro Features</div>
    <div class="upgrade-btn">Subsribe Now</div>
  </div>
  <div class="copyright">Copyright @ 2024</div>
</aside>

<h1 class="page-title">Dashboard</h1>
<div class="search">Search...<svg width="14" height="14" viewBox="0 0 24 24" fill="none" stroke="#111" stroke-width="2.5"><circle cx="10" cy="10" r="7"/><path d="M15 15l6 6"/></svg></div>
<div class="round-btn" style="left:1027px">EN</div>
<div class="round-btn" style="left:1073px"><svg width="16" height="16" viewBox="0 0 24 24" fill="none" stroke="#111" stroke-width="2"><path d="M6 17V10a6 6 0 0112 0v7l2 2H4zM10 21h4"/></svg></div>
<div class="round-btn" style="left:1118px"><svg width="16" height="16" viewBox="0 0 24 24" fill="none" stroke="#111" stroke-width="2"><circle cx="12" cy="7" r="4"/><path d="M4 22c0-5 4-8 8-8s8 3 8 8"/></svg></div>

<div class="map" role="img" aria-label="World map of the Atlantic region showing event locations marked with red pins in Brazil, Senegal, Italy and Ethiopia"></div>
<div class="map-tool" style="top:240px"><svg width="16" height="16" viewBox="0 0 24 24" fill="none" stroke="#111" stroke-width="2.5"><path d="M3 8V3h5M16 3h5v5M21 16v5h-5M8 21H3v-5"/></svg></div>
<div class="map-tool" style="top:280px"><svg width="16" height="16" viewBox="0 0 24 24" fill="none" stroke="#111" stroke-width="2"><rect x="3" y="3" width="18" height="18" stroke-dasharray="3 2"/><path d="M8 17v-5l4-3 4 3v5z"/></svg></div>
<div class="map-tool" style="top:320px"><svg width="16" height="16" viewBox="0 0 24 24" fill="none" stroke="#111" stroke-width="2.5"><path d="M2 12s4-6 10-6 10 6 10 6-4 6-10 6S2 12 2 12z"/><circle cx="12" cy="12" r="2.5"/></svg></div>
<div class="map-tool" style="top:361px"><svg width="18" height="18" viewBox="0 0 24 24" fill="none" stroke="#111" stroke-width="2"><circle cx="12" cy="12" r="9"/><path d="M9.5 9.5a2.5 2.5 0 015 0c0 2-2.5 2-2.5 4M12 17v.5"/></svg></div>
<div class="map-tool" style="top:402px"><svg width="15" height="15" viewBox="0 0 24 24" fill="none" stroke="#111" stroke-width="2.5"><circle cx="10" cy="10" r="7"/><path d="M15 15l6 6"/></svg></div>

<section class="card" style="top:585px">
  <svg style="position:absolute;left:17px;top:27px" width="48" height="66" viewBox="0 0 48 66" fill="none" stroke="#111" stroke-width="5"><circle cx="24" cy="15" r="12"/><path d="M4 64V54c0-10 8-17 20-17s20 7 20 17v10"/></svg>
  <div class="card-label" style="left:86px;top:27px">Affected People</div>
  <div class="stat">1.200.136</div>
</section>
<section class="card" style="top:718px">
  <svg style="position:absolute;left:25px;top:35px" width="58" height="52" viewBox="0 0 58 52" fill="none" stroke="#111" stroke-width="5"><path d="M29 4L3 48h52z" stroke-linejoin="round"/><path d="M29 18v16M29 39v4"/></svg>
  <div class="card-label" style="left:106px;top:27px">Alert</div>
  <div class="alert-text">Heavy rain on<br>Area - Source</div>
</section>

<div class="events-label">Event Ongoing</div>
<div class="event" style="top:610px"><div class="event-type">Flood</div><div class="event-meta">Area 1 - DD/MM/YYYY</div></div>
<div class="event" style="top:684px"><div class="event-type">Flood</div><div class="event-meta">Area 2 - DD/MM/YYYY</div></div>
<div class="event" style="top:758px"><div class="event-type">Flood</div><div class="event-meta">Area 3 - DD/MM/YYYY</div></div>
<div class="event" style="top:832px"><div class="event-type">Flood</div></div>
<div class="scroll-track"></div>
<div class="scroll-thumb"></div>
</body>
</html>
```